iOS App Design Project for Pebble Notes

We are looking for a redesign of the UI for our app, Pebble Notes. The app is a to-do list type app with 4 screens, and we already have a UI for it but we would like a nicer looking one that has a better colour scheme and is more intuitive.

We would like something that is a real treat to look at, and that users really want to use. Essentially what we want is the nicest and most simple design possible, as the current UI we have is not very user friendly.

The app is already on the market and is free so if you have an iOS device you can download it and take a look at it, and we have also included screenshots of the app.
Updates

Project Deadline Extended
Reason: I am updating the design brief and will also guarantee the payment.

Target Market(s)

Mobile users looking for simplicity

Requirements
Must have
• - Very visually pleasing
- Simple layout with minimal clutter
- Icons and buttons that explain what they do
Should not have
• Any features that detract from the simplicity of the app are not wanted.

```html
<!DOCTYPE html>
<html lang="en">
<head>
<meta charset="utf-8">
<title>Pebble Notes – Task</title>
<link rel="stylesheet" href="https://fonts.googleapis.com/css2?family=Arimo:wght@400;700&display=swap">
<style>
  :root {
    --page: #f1f1f1;
    --status-black: #050505;
    --nav-top: #5a8ec4;
    --nav-bottom: #1f5a9a;
    --paper: #f2eee6;
    --paper-low: #e9e4d8;
    --rule: #c3d2e4;
    --margin-red: #e59a85;
    --ink: #2c2c2c;
    --tag-orange: #f26a35;
    --tag-blue: #4aa3e3;
    --tag-green: #4cb548;
    --info-grey: #7a7a7a;
    --button-red: #c7282c;
    --button-red-dark: #9d1c20;
    --button-cross: #4a1214;
    --ad-dark: #262626;
    --tab-top: #2c67a8;
    --tab-bottom: #164b86;
    --tab-dim: #0f3a6b;
    --white: #ffffff;
  }
  * { box-sizing: border-box; margin: 0; padding: 0; }
  html, body { width: 1200px; height: 1000px; overflow: hidden; }
  body {
    background: var(--page);
    font-family: "Arimo", Arial, sans-serif;
    position: relative;
  }
  .screen {
    position: absolute;
    left: 280px; top: 20px;
    width: 640px; height: 960px;
    overflow: hidden;
    background: var(--paper);
    box-shadow: 0 6px 24px rgba(0,0,0,.18);
  }
  .status-bar {
    height: 40px;
    background: var(--status-black);
    color: var(--white);
    display: flex; align-items: center; justify-content: space-between;
    padding: 0 12px;
    font-size: 24px; font-weight: 700;
    position: relative;
  }
  .status-left, .status-right { display: flex; align-items: center; gap: 8px; }
  .status-time { position: absolute; left: 50%; transform: translateX(-50%); }
  .nav-bar {
    height: 88px;
    background: linear-gradient(var(--nav-top), var(--nav-bottom));
    display: flex; align-items: center; justify-content: center;
    border-bottom: 1px solid #17497f;
  }
  .nav-title { color: var(--white); font-size: 40px; font-weight: 400; text-shadow: 0 -1px 0 rgba(0,0,0,.3); }
  .task-sheet {
    position: absolute; left: 0; top: 128px; width: 640px; height: 636px;
    background:
      linear-gradient(90deg, transparent 94px, var(--margin-red) 94px, var(--margin-red) 96px, transparent 96px),
      repeating-linear-gradient(transparent 0 59px, var(--rule) 59px 60px),
      linear-gradient(var(--paper), var(--paper-low));
  }
  .task-list { list-style: none; }
  .task-row {
    height: 60px; display: flex; align-items: center;
    padding-left: 120px; padding-right: 24px;
    font-size: 34px; color: var(--ink);
  }
  .task-name { flex: 1; }
  .task-tag { width: 70px; height: 38px; margin-right: 28px; }
  .task-info { width: 44px; height: 44px; }
  .add-task-button {
    position: absolute; left: 300px; top: 562px;
    width: 180px; height: 112px; border-radius: 12px;
    background: linear-gradient(#d83b3c, var(--button-red) 55%, var(--button-red-dark));
    box-shadow: 0 4px 8px rgba(0,0,0,.45), inset 0 1px 0 rgba(255,255,255,.35);
    display: flex; align-items: center; justify-content: center;
    z-index: 2;
  }
  .ad-band {
    position: absolute; left: 0; top: 764px; width: 640px; height: 100px;
    background: repeating-linear-gradient(135deg, var(--ad-dark) 0 3px, #2c2c2c 3px 6px);
    color: var(--white); font-size: 30px; font-weight: 700;
    display: flex; align-items: center; justify-content: center;
  }
  .tab-bar {
    position: absolute; left: 0; bottom: 0; width: 640px; height: 96px;
    background: linear-gradient(var(--tab-top), var(--tab-bottom));
    display: flex;
  }
  .tab-item {
    flex: 1; display: flex; flex-direction: column; align-items: center; justify-content: center;
    gap: 4px; color: var(--white); font-size: 20px; font-weight: 700;
  }
  .tab-item.is-active { color: var(--tab-dim); }
  .tab-item svg { width: 52px; height: 52px; }
</style>
</head>
<body>
<main class="screen">
  <header class="status-bar">
    <div class="status-left">
      <svg width="34" height="20" viewBox="0 0 34 20" aria-hidden="true">
        <rect x="0" y="14" width="4" height="6" fill="#fff"/><rect x="6" y="10" width="4" height="10" fill="#fff"/>
        <rect x="12" y="17" width="4" height="3" fill="#fff"/><rect x="18" y="17" width="4" height="3" fill="#fff"/><rect x="24" y="17" width="4" height="3" fill="#fff"/>
      </svg>
      <span>Ridgeway</span>
      <svg width="28" height="22" viewBox="0 0 28 22" aria-hidden="true">
        <path d="M2 8 A17 17 0 0 1 26 8" stroke="#fff" stroke-width="3" fill="none"/>
        <path d="M7 13 A10 10 0 0 1 21 13" stroke="#fff" stroke-width="3" fill="none"/>
        <circle cx="14" cy="18" r="3" fill="#fff"/>
      </svg>
    </div>
    <span class="status-time">7:29 PM</span>
    <div class="status-right">
      <svg width="18" height="18" viewBox="0 0 18 18" aria-hidden="true"><path d="M17 1 L1 8 L8 10 L10 17 Z" fill="#fff"/></svg>
      <span>30%</span>
      <svg width="46" height="22" viewBox="0 0 46 22" aria-hidden="true">
        <rect x="1" y="2" width="38" height="18" rx="3" stroke="#fff" stroke-width="2" fill="none"/>
        <rect x="41" y="7" width="4" height="8" fill="#fff"/>
        <rect x="4" y="5" width="11" height="12" fill="#fff"/>
      </svg>
    </div>
  </header>

  <nav class="nav-bar"><h1 class="nav-title">Task</h1></nav>

  <section class="task-sheet">
    <ul class="task-list">
      <li class="task-row">
        <span class="task-name">Hello</span>
        <svg class="task-tag" viewBox="0 0 70 38" aria-label="Orange tag"><path d="M18 2 H66 a3 3 0 0 1 3 3 V33 a3 3 0 0 1 -3 3 H18 L2 19 Z" fill="var(--tag-orange)"/><circle cx="15" cy="19" r="3" fill="#fff"/></svg>
        <svg class="task-info" viewBox="0 0 44 44" aria-label="Details"><circle cx="22" cy="22" r="20" fill="var(--info-grey)"/><circle cx="22" cy="13" r="3" fill="#fff"/><rect x="19" y="19" width="6" height="15" fill="#fff"/></svg>
      </li>
      <li class="task-row">
        <span class="task-name">Hello 2</span>
        <svg class="task-tag" viewBox="0 0 70 38" aria-label="Blue tag"><path d="M18 2 H66 a3 3 0 0 1 3 3 V33 a3 3 0 0 1 -3 3 H18 L2 19 Z" fill="var(--tag-blue)"/><circle cx="15" cy="19" r="3" fill="#fff"/></svg>
        <svg class="task-info" viewBox="0 0 44 44" aria-label="Details"><circle cx="22" cy="22" r="20" fill="var(--info-grey)"/><circle cx="22" cy="13" r="3" fill="#fff"/><rect x="19" y="19" width="6" height="15" fill="#fff"/></svg>
      </li>
      <li class="task-row">
        <span class="task-name">Hello 3</span>
        <svg class="task-tag" viewBox="0 0 70 38" aria-label="Green tag"><path d="M18 2 H66 a3 3 0 0 1 3 3 V33 a3 3 0 0 1 -3 3 H18 L2 19 Z" fill="var(--tag-green)"/><circle cx="15" cy="19" r="3" fill="#fff"/></svg>
        <svg class="task-info" viewBox="0 0 44 44" aria-label="Details"><circle cx="22" cy="22" r="20" fill="var(--info-grey)"/><circle cx="22" cy="13" r="3" fill="#fff"/><rect x="19" y="19" width="6" height="15" fill="#fff"/></svg>
      </li>
    </ul>
  </section>

  <div class="add-task-button" aria-label="Add task">
    <svg width="60" height="60" viewBox="0 0 60 60" aria-hidden="true">
      <rect x="24" y="4" width="12" height="52" fill="var(--button-cross)"/>
      <rect x="4" y="24" width="52" height="12" fill="var(--button-cross)"/>
    </svg>
  </div>

  <aside class="ad-band">Advertising</aside>

  <footer class="tab-bar">
    <div class="tab-item">
      <svg viewBox="0 0 52 52" aria-hidden="true" fill="none" stroke="#fff" stroke-width="3">
        <path d="M4 10 l4 4 l7 -9"/><line x1="20" y1="10" x2="48" y2="10"/>
        <rect x="5" y="21" width="9" height="9"/><line x1="20" y1="26" x2="48" y2="26"/>
        <rect x="5" y="37" width="9" height="9"/><line x1="20" y1="42" x2="48" y2="42"/>
      </svg>
      <span>List</span>
    </div>
    <div class="tab-item is-active">
      <svg viewBox="0 0 52 52" aria-hidden="true" fill="none" stroke="var(--tab-dim)" stroke-width="3">
        <rect x="5" y="8" width="42" height="38" rx="3"/><line x1="5" y1="17" x2="47" y2="17"/>
        <line x1="15" y1="3" x2="15" y2="12"/><line x1="37" y1="3" x2="37" y2="12"/>
        <path d="M15 31 l8 8 l16 -16" stroke-width="5"/>
      </svg>
      <span>Task</span>
    </div>
    <div class="tab-item">
      <svg viewBox="0 0 52 52" aria-hidden="true" fill="none" stroke="#fff" stroke-width="3">
        <path d="M6 4 H30 L38 12 V48 H6 Z"/>
        <line x1="12" y1="20" x2="32" y2="20"/><line x1="12" y1="27" x2="32" y2="27"/><line x1="12" y1="34" x2="32" y2="34"/><line x1="12" y1="41" x2="26" y2="41"/>
        <path d="M44 8 l5 3 l-12 26 l-5 3 l0 -6 Z"/>
      </svg>
      <span>Notes</span>
    </div>
    <div class="tab-item">
      <svg viewBox="0 0 52 52" aria-hidden="true">
        <circle cx="26" cy="26" r="22" fill="#fff"/>
        <rect x="23" y="12" width="6" height="28" fill="var(--tab-bottom)"/>
        <rect x="12" y="23" width="28" height="6" fill="var(--tab-bottom)"/>
      </svg>
      <span>More</span>
    </div>
  </footer>
</main>
</body>
</html>
```